REDESIGN SIGN UP PAGE - EASY TO READ AND UNDERSTAND QUICKLY

I need to redesign my sign up page DESKTOP AND MOBILE VERSION to include 2 products that are each available as a monthly subscription, 6 mth or 12 mth subscription.

Currently I only promote one product on my website but now will be two. https://www.brightlanepromoworks.biz/signup

Now I will have two products:

1. UNLIMITED VACATION CERTIFICATES, DINING VOUCHERS & SAVINGS INCENTIVES
Unlimited Monthly Plan $99 / Month + $199 One-Time Set-Up Fee
Unlimited Bi Annual Plan $490 / 6 Months + $199 One-Time Set-Up Fee
Unlimited Annual Plan $898 / 12 Months + $199 One-Time Set-Up Fee

2. UNLIMITED SMART DEVICE INCENTIVES & OTHER HARD PREMIUMS
Unlimited Monthly Plan $299 / Month + $199 One-Time Set-Up Fee
Unlimited Bi Annual Plan $1,590 / 6 Months + $199 One-Time Set-Up Fee
Unlimited Annual Plan $2,898 / 12 Months + $199 One-Time Set-Up Fee

When promoting the different plans you can see the different categories of incentives I offer here: https://www.brightlanepromoworks.biz/incentives

The SMART DEVICE CERTIFICATES & INCENTIVES category is for product #2 and all the rest of the Categories is for Product #1 Feel free to use images as a visual so customers can see that this product includes Vacations & Restaurants and this product includes only smart devices....

USE ALL CURRENT BULLET POINTS FOR BOTH PLANS THAT IS CURRENTLY ON WEBSITE. USE ALL CURRENT CONTENT ON WEBSITE ORIGINAL SIGN UP PAGE. DO NOT LEAVE ANY CONTENT OUT.

Target Market(s)

BUSINESS OWNERS

Industry/Entity Type

Marketing

Number of Pages Required

2 page

Requirements
Must have
• When promoting the 2 different products on the new sign up page you can see the different categories of incentives I offer here: https://www.brightlanepromoworks.biz/incentives fee; free to use images to showcase what each product offers.

The SMART DEVICE CERTIFICATES & INCENTIVES category is for product #2 and all the rest of the Categories is for Product #1

I want the user to easily understand we have two products that are available in 3 ways, monthly subscription, bi annual and annual and can see the price immediately for all 3 options for both products without toggling, etc.

Must be super clean easy to ready design. Not too busy at all please
Nice to have
• USE ALL CURRENT BULLET POINTS FOR BOTH PLANS THAT IS CURRENTLY ON WEBSITE. USE ALL CURRENT CONTENT ON WEBSITE ORIGINAL SIGN UP PAGE. DO NOT LEAVE ANY CONTENT OUT.

Should not have

```html
<!DOCTYPE html>
<html lang="en">
<head>
<meta charset="utf-8">
<title>Sign Up – Brightlane Promoworks</title>
<link href="https://fonts.googleapis.com/css2?family=Montserrat:ital,wght@0,400;0,500;0,600;0,700;0,800;0,900;1,400&family=Poppins:wght@400;500;600&display=swap" rel="stylesheet">
<style>
:root{
  --brand-blue:#1b75c4;
  --nav-blue:#1f6fc0;
  --dark-box:#3a3f47;
  --call-green:#4db04a;
  --ink:#111418;
  --grey-text:#5b5f66;
  --orange-1:#f6a623;
  --orange-2:#fcc24a;
  --green-1:#4cb050;
  --green-2:#2f8a36;
  --red-1:#ee1c25;
  --red-2:#b4161d;
  --blue-1:#1a7ac8;
  --blue-2:#0f4f8e;
  --footer:#17212d;
  --footer-text:#c6ccd4;
  --accent-green:#58c23f;
  --chat-red:#e8232b;
}
*{box-sizing:border-box;margin:0;padding:0}
html,body{width:1200px;height:2799px;overflow:hidden;background:#fff}
body{position:relative;font-family:'Poppins',sans-serif;color:var(--ink)}

/* Header */
.site-header{position:absolute;left:0;top:0;width:1200px;height:69px;background:var(--nav-blue)}
.site-header .logo-zone{position:absolute;left:0;top:0;height:69px;width:330px;background:#fff;clip-path:polygon(0 0,100% 0,93% 100%,0 100%)}
.brand{position:absolute;left:20px;top:22px;display:flex;align-items:center;gap:9px;font-family:'Montserrat',sans-serif;font-weight:700;font-size:19px;color:var(--brand-blue);letter-spacing:.2px}
.brand .dot{width:20px;height:20px;border-radius:50%;background:var(--brand-blue)}
.main-nav{position:absolute;left:359px;top:28px;display:flex;gap:15px;font-size:11px;color:#fff}
.user-box{position:absolute;top:0;height:69px;display:flex;flex-direction:column;align-items:center;justify-content:center;gap:5px;color:#fff;font-size:10px;text-transform:uppercase}
.user-box.login{left:849px;width:67px;background:var(--dark-box)}
.user-box.signup{left:916px;width:69px;background:var(--nav-blue)}
.call-box{position:absolute;left:985px;top:0;width:215px;height:69px;background:var(--call-green);color:#fff;font-family:'Montserrat',sans-serif;font-weight:700;font-size:10.5px;display:flex;align-items:center;gap:12px;padding-left:10px;line-height:1.6}

/* Hero */
.hero{position:absolute;left:0;top:69px;width:1200px;height:406px;background:linear-gradient(90deg,var(--orange-1),var(--orange-2))}
.hero h1{position:absolute;left:92px;top:166px;font-family:'Montserrat',sans-serif;font-weight:900;font-size:72px;color:#fff;letter-spacing:-1px}
.hero-photo{position:absolute;left:520px;top:0;width:640px;height:406px;background:radial-gradient(ellipse at 55% 55%,rgba(255,236,214,.55),rgba(252,194,74,0) 65%)}

/* Intro */
.intro{position:absolute;left:0;top:575px;width:1200px;text-align:center}
.intro h2{font-family:'Montserrat',sans-serif;font-weight:900;font-size:42px;line-height:58px;letter-spacing:-.8px;text-transform:uppercase;color:var(--ink)}
.intro h2 span{color:var(--brand-blue)}
.intro p{margin-top:37px;font-family:'Montserrat',sans-serif;font-size:26px;line-height:42px;color:var(--grey-text)}

/* Plans */
.plan{position:absolute;top:921px;width:337px;height:1322px;border-radius:34px;border:3px solid;overflow:hidden;color:#fff;text-align:center}
.plan.monthly{left:71px;border-color:var(--green-1);background:linear-gradient(180deg,var(--green-1),var(--green-2))}
.plan.biannual{left:431px;border-color:var(--red-1);background:linear-gradient(180deg,var(--red-1),var(--red-2))}
.plan.annual{left:792px;border-color:var(--blue-1);background:linear-gradient(180deg,var(--blue-1),var(--blue-2))}
.plan .price-cap{position:absolute;left:0;top:0;width:100%;height:200px}
.plan .prices{position:absolute;left:0;top:22px;width:100%;display:flex}
.plan .product{flex:1;display:flex;flex-direction:column;align-items:center}
.plan .product + .product{border-left:1px solid #e1e3e6}
.plan .product-name{font-family:'Montserrat',sans-serif;font-weight:700;font-size:9.5px;line-height:12px;letter-spacing:.3px;text-transform:uppercase;color:#6a6e75;height:26px}
.plan .price{font-family:'Montserrat',sans-serif;font-weight:800;font-size:42px;line-height:52px;color:#3c3f46;letter-spacing:-1px}
.plan .price-note{font-family:'Montserrat',sans-serif;font-style:italic;font-size:10.5px;line-height:14px;color:#6a6e75;margin-top:4px}
.plan .kicker{position:absolute;left:0;top:227px;width:100%;font-size:14px;font-weight:500}
.plan h3{position:absolute;left:0;top:243px;width:100%;font-family:'Montserrat',sans-serif;font-weight:800;font-size:48px}
.plan ul{position:absolute;left:30px;top:323px;width:265px;list-style:none}
.plan li{height:42.9px;line-height:42px;font-size:11px;border-bottom:1px solid rgba(255,255,255,.22);white-space:nowrap}
.plan li:last-child{border-bottom:none}
.plan .select{position:absolute;left:85px;top:1210px;width:161px;height:51px;border-radius:26px;background:#fff;color:var(--ink);font-family:'Montserrat',sans-serif;font-weight:700;font-size:16px;line-height:51px}

/* Footer */
.site-footer{position:absolute;left:0;top:2338px;width:1200px;height:461px;background:var(--footer);color:var(--footer-text);font-size:12.3px}
.footer-brand{position:absolute;left:92px;top:78px;width:240px;font-family:'Montserrat',sans-serif;font-weight:700;font-size:20px;color:var(--brand-blue);display:flex;align-items:center;gap:9px;line-height:1.2}
.footer-brand .dot{width:22px;height:22px;border-radius:50%;background:var(--brand-blue);flex:none}
.socials{position:absolute;left:124px;top:159px;display:flex;gap:8px}
.socials span{width:38px;height:38px;border-radius:50%;background:#5b636e}
.samples-btn{position:absolute;left:96px;top:219px;width:230px;height:48px;background:var(--accent-green);color:#fff;text-align:center;font-family:'Montserrat',sans-serif;font-weight:800;font-size:14px;line-height:18px;padding-top:6px;clip-path:polygon(0 0,100% 0,99% 88%,50% 100%,1% 88%)}
.samples-btn small{display:block;font-weight:500;font-size:12px}
.divider{position:absolute;top:55px;width:1px;height:250px;background:rgba(255,255,255,.1)}
.col{position:absolute;top:62px}
.col h4{font-family:'Montserrat',sans-serif;font-weight:900;font-size:15px;color:#fff;text-transform:uppercase;letter-spacing:-.2px;margin-bottom:22px}
.col.links a{display:block;color:var(--footer-text);text-decoration:none;line-height:25px;white-space:nowrap}
.col.links a.wrap{white-space:normal;line-height:17px}
.contact-row{display:flex;gap:8px;margin-bottom:8px;line-height:17.5px}
.contact-row svg{flex:none;margin-top:2px}
.contact-row b{color:#fff;font-weight:600}
.accent{color:var(--accent-green)}
.legal{position:absolute;left:92px;top:429px;font-size:12.3px;color:var(--footer-text)}
.legal b{color:#fff;font-weight:600}
.legal .hl{color:var(--brand-blue)}
.policy{position:absolute;right:89px;top:429px;font-size:12.3px}
.chat{position:absolute;left:1126px;top:397px;width:46px;height:46px;border-radius:50%;background:var(--chat-red);display:flex;align-items:center;justify-content:center}
</style>
</head>
<body>

<header class="site-header">
  <div class="logo-zone"></div>
  <div class="brand"><span class="dot"></span>Brightlane Promoworks</div>
  <nav class="main-nav">
    <span>Home</span><span>The Incentives</span><span>Samples</span><span>Industries</span><span>Testimonials</span><span>Faq</span><span>Integrations</span>
  </nav>
  <div class="user-box login">
    <svg width="14" height="14" viewBox="0 0 14 14"><circle cx="7" cy="4" r="3.3" fill="#fff"/><path d="M1 14c0-4 3-6 6-6s6 2 6 6z" fill="#fff"/></svg>Login
  </div>
  <div class="user-box signup">
    <svg width="16" height="16" viewBox="0 0 16 16"><circle cx="8" cy="8" r="7" fill="none" stroke="#fff" stroke-width="1.5"/><path d="M8 4l3.5 4H9.3v4H6.7V8H4.5z" fill="#fff"/></svg>Sign Up
  </div>
  <div class="call-box">
    <svg width="17" height="30" viewBox="0 0 17 30"><rect x="1" y="1" width="15" height="28" rx="3" fill="none" stroke="#fff" stroke-width="2"/><circle cx="8.5" cy="24.5" r="1.6" fill="#fff"/></svg>
    <div>CALL US: 1-555-204-7731<br>TEXT US: 1-555-381-6645</div>
  </div>
</header>

<section class="hero">
  <h1>SAVINGS</h1>
  <div class="hero-photo" role="img" aria-label="Smiling woman holding a piggy bank and a fan of banknotes"></div>
</section>

<section class="intro">
  <h2>Congratulations on making the decision<br>to <span>make more money for your business</span></h2>
  <p>This program is an online subscription based incentive marketing<br>system with the following features</p>
</section>

<!-- Monthly -->
<article class="plan monthly">
  <svg class="price-cap" viewBox="0 0 337 200" preserveAspectRatio="none"><path d="M0 0H337V155C280 150 240 197 168 197S57 150 0 155Z" fill="#fff"/></svg>
  <div class="prices">
    <div class="product"><div class="product-name">Vacations, Dining<br>&amp; Savings</div><div class="price">$99</div><div class="price-note">Month + $199<br>One-Time Set-Up Fee</div></div>
    <div class="product"><div class="product-name">Smart Devices<br>&amp; Hard Premiums</div><div class="price">$299</div><div class="price-note">Month + $199<br>One-Time Set-Up Fee</div></div>
  </div>
  <div class="kicker">Unlimited Plan</div>
  <h3>MONTHLY</h3>
  <ul>
    <li>Unlimited E-Certificates</li><li>Unlimited SMS Certificates</li><li>Unlimited Web Banner Certificates</li><li>Unlimited White Label Certificate Landing Pages</li><li>Unlimited Website Sticky Bar Certificates</li><li>Unlimited Website Pop Up Certificate</li><li>Unlimited API E-Certificates</li><li>Unlimited Flowlink Integration Access</li><li>FREE Warm Lead Letter Templates</li><li>FREE Customer Appreciation Letter Templates</li><li>FREE Professional-Grade Incentive Videos</li><li>FREE Proven Social Feed Ad Templates</li><li>FREE High-Converting Banner Ad Templates</li><li>FREE Time-Tested Print Ad Templates</li><li>FREE White Label Redemption Website</li><li>FREE Industry Specific Ad Packs</li><li>FREE Affiliate Program-Earn 50% Commissions</li><li>FREE Eye-Catching Posters, Flyers &amp; Brochures</li><li>Each Certificate</li><li>FREE Step by Step Redemption Guides</li>
  </ul>
  <div class="select">SELECT</div>
</article>

<!-- Bi annual -->
<article class="plan biannual">
  <svg class="price-cap" viewBox="0 0 337 200" preserveAspectRatio="none"><path d="M0 0H337V155C280 150 240 197 168 197S57 150 0 155Z" fill="#fff"/></svg>
  <div class="prices">
    <div class="product"><div class="product-name">Vacations, Dining<br>&amp; Savings</div><div class="price">$490</div><div class="price-note">6 Months + $199<br>One-Time Set-Up Fee</div></div>
    <div class="product"><div class="product-name">Smart Devices<br>&amp; Hard Premiums</div><div class="price">$1,590</div><div class="price-note">6 Months + $199<br>One-Time Set-Up Fee</div></div>
  </div>
  <div class="kicker">Unlimited Plan</div>
  <h3>BI ANNUAL</h3>
  <ul>
    <li>Unlimited E-Certificates</li><li>Unlimited SMS Certificates</li><li>Unlimited Web Banner Certificates</li><li>Unlimited White Label Certificate Landing Pages</li><li>Unlimited Website Sticky Bar Certificates</li><li>Unlimited Website Pop Up Certificate</li><li>Unlimited API E-Certificates</li><li>Unlimited Flowlink Integration Access</li><li>FREE Warm Lead Letter Templates</li><li>FREE Customer Appreciation Letter Templates</li><li>FREE Professional-Grade Incentive Videos</li><li>FREE Proven Social Feed Ad Templates</li><li>FREE High-Converting Banner Ad Templates</li><li>FREE Time-Tested Print Ad Templates</li><li>FREE White Label Redemption Website</li><li>FREE Industry Specific Ad Packs</li><li>FREE Affiliate Program-Earn 50% Commissions</li><li>FREE Eye-Catching Posters, Flyers &amp; Brochures</li><li>Each Certificate</li><li>FREE Step by Step Redemption Guides</li>
  </ul>
  <div class="select">SELECT</div>
</article>

<!-- Annual -->
<article class="plan annual">
  <svg class="price-cap" viewBox="0 0 337 200" preserveAspectRatio="none"><path d="M0 0H337V155C280 150 240 197 168 197S57 150 0 155Z" fill="#fff"/></svg>
  <div class="prices">
    <div class="product"><div class="product-name">Vacations, Dining<br>&amp; Savings</div><div class="price">$898</div><div class="price-note">12 Months + $199<br>One-Time Set-Up Fee</div></div>
    <div class="product"><div class="product-name">Smart Devices<br>&amp; Hard Premiums</div><div class="price">$2,898</div><div class="price-note">12 Months + $199<br>One-Time Set-Up Fee</div></div>
  </div>
  <div class="kicker">Unlimited Plan</div>
  <h3>ANNUAL</h3>
  <ul>
    <li>Unlimited E-Certificates</li><li>Unlimited SMS Certificates</li><li>Unlimited Web Banner Certificates</li><li>Unlimited White Label Certificate Landing Pages</li><li>Unlimited Website Sticky Bar Certificates</li><li>Unlimited Website Pop Up Certificate</li><li>Unlimited API E-Certificates</li><li>Unlimited Flowlink Integration Access</li><li>FREE Warm Lead Letter Templates</li><li>FREE Customer Appreciation Letter Templates</li><li>FREE Professional-Grade Incentive Videos</li><li>FREE Proven Social Feed Ad Templates</li><li>FREE High-Converting Banner Ad Templates</li><li>FREE Time-Tested Print Ad Templates</li><li>FREE White Label Redemption Website</li><li>FREE Industry Specific Ad Packs</li><li>FREE Affiliate Program-Earn 50% Commissions</li><li>FREE Eye-Catching Posters, Flyers &amp; Brochures</li><li>Each Certificate</li><li>FREE Step by Step Redemption Guides</li>
  </ul>
  <div class="select">SELECT</div>
</article>

<footer class="site-footer">
  <div class="footer-brand"><span class="dot"></span>Brightlane Promoworks</div>
  <div class="socials"><span></span><span></span><span></span><span></span></div>
  <div class="samples-btn">GET FREE SAMPLES<small>100% FREE</small></div>

  <div class="divider" style="left:353px"></div>
  <div class="divider" style="left:679px"></div>
  <div class="divider" style="left:874px"></div>

  <div class="col" style="left:376px;width:290px">
    <h4>Contact Us</h4>
    <div class="contact-row">
      <svg width="13" height="15" viewBox="0 0 13 15"><path d="M6.5 1a5 5 0 0 0-5 5c0 3.5 5 8 5 8s5-4.5 5-8a5 5 0 0 0-5-5z" fill="none" stroke="#9aa3ae" stroke-width="1.2"/><circle cx="6.5" cy="6" r="1.8" fill="none" stroke="#9aa3ae" stroke-width="1.2"/></svg>
      <div><b>Brightlane Promoworks Group, Inc.</b><br>4470 Harbor Ridge Road Suite 310<br>Port Alden, CA 90000</div>
    </div>
    <div class="contact-row">
      <svg width="14" height="14" viewBox="0 0 14 14"><path d="M3 1l2.5 3-1.5 1.5a8 8 0 0 0 4.5 4.5L10 8.5l3 2.5-1.5 2C6 13 1 8 1 2.5z" fill="none" stroke="#9aa3ae" stroke-width="1.2"/></svg>
      <div>USA Office: <b>1-555-204-7731</b><br>International: <b>1-800-555-0142</b><br>Text Us: <b>1-555-318-2260</b></div>
    </div>
    <div class="contact-row">
      <svg width="14" height="12" viewBox="0 0 14 12"><rect x="1" y="1" width="12" height="10" fill="none" stroke="#9aa3ae" stroke-width="1.2"/><path d="M1 1l6 5 6-5" fill="none" stroke="#9aa3ae" stroke-width="1.2"/></svg>
      <div>info@brightlanepromoworks.biz</div>
    </div>
    <div class="contact-row">
      <svg width="14" height="14" viewBox="0 0 14 14"><circle cx="7" cy="7" r="6" fill="none" stroke="#9aa3ae" stroke-width="1.2"/><path d="M7 3.5V7l2.5 1.5" fill="none" stroke="#9aa3ae" stroke-width="1.2"/></svg>
      <div>24/7 Chat Support<br>24/7 Live Answering Service<br>24/7 Email Support<br><span class="accent">Live Phone &amp; SMS Support:</span><br>Monday - Friday 8am - 5pm PST<br><span class="accent">Sat/Sun/Holidays Closed</span></div>
    </div>
  </div>

  <div class="col links" style="left:702px;width:165px">
    <h4>Quick Links</h4>
    <a>Home</a><a>The Incentives</a><a>Samples</a><a>Affiliate</a><a>Testimonials</a><a>Faq</a><a>Contact Us</a><a>Redemption Demo Videos</a><a class="wrap" style="margin-top:4px">BPW Distribute Certificate Demo Videos</a>
  </div>

  <div class="col links" style="left:896px;width:220px">
    <h4>Other Links</h4>
    <a>Hoteliers</a><a>BPW Certificates List</a><a>How To Use BPW Certificates</a><a>Social Feed Incentive Campaign</a><a>Pop Ups &amp; Sticky Bars</a><a>Whitepaper - Increase Sales</a><a class="wrap" style="margin:4px 0 6px">Whitepaper - Improve Sales During Strange Times</a><a class="wrap">Whitepaper - Boost Website Conversions</a>
  </div>

  <div class="legal">© 2020 <b>Brightlane Promoworks Group, Inc.</b> All Rights Reserved. CST# 4408172 <span class="hl">TCRC#</span> 738204</div>
  <div class="policy">Privacy Policy &nbsp;|&nbsp; Term And Conditions</div>
  <div class="chat"><svg width="20" height="20" viewBox="0 0 20 20"><rect x="2" y="2" width="16" height="16" rx="3" fill="#fff"/><path d="M6 12c2 1.5 6 1.5 8 0" stroke="var(--chat-red)" stroke-width="1.6" fill="none"/></svg></div>
</footer>

</body>
</html>
```